Need help in designing new business card utilizing our new logo.

Veltrix Solutions works with Construction Business Owners, Managers & IT Professionals to strengthen software usage and increase user productivity.

Our Construction Accounting and Mobile Field Management Software Clients engage with us in the following areas:

New Software Implementations
Software Re-Implementations
Redesigning Software Usage at the User Level
Project Coordination & Management
Continued Software Support

Old tag line:
Weighing Options - Implementing Solutions

www.veltrix-solutions.example

Quad Shift is a product, but not needed for a new business card.

```html
<!DOCTYPE html>
<html lang="en">
<head>
<meta charset="utf-8">
<title>Veltrix Solutions – Business Card</title>
<link href="https://fonts.googleapis.com/css2?family=Ubuntu:wght@400;500;700&display=swap" rel="stylesheet">
<style>
  :root {
    --page: #e8e5e2;
    --card-top: #f4f4f4;
    --brand-blue: #0f1aa0;
    --strip-light: #dcdcdc;
    --strip-dark: #bcbcbc;
    --white: #ffffff;
    --faint: rgba(15, 26, 160, 0.22);
  }
  * { box-sizing: border-box; margin: 0; padding: 0; }
  html, body {
    width: 1200px; height: 918px; overflow: hidden;
    background: var(--page);
    font-family: "Ubuntu", sans-serif;
  }
  .canvas { position: relative; width: 1200px; height: 918px; }

  .card {
    position: absolute; width: 522px; height: 322px;
    background: var(--card-top);
    box-shadow: 0 6px 18px rgba(0,0,0,0.12);
    overflow: hidden;
  }
  .card--front { left: 174px; top: 142px; }
  .card--back  { left: 502px; top: 488px; }

  .card__head {
    height: 171px; display: flex; align-items: center; justify-content: center; gap: 16px;
  }
  .brand-mark { width: 34px; height: 34px; background: var(--brand-blue); }
  .brand-name {
    font-weight: 700; font-size: 36px; color: var(--brand-blue); letter-spacing: 0.5px;
  }
  .card--back .brand-mark { background: var(--faint); }
  .card--back .brand-name { color: var(--faint); }
  .card--back .card__head { transform: scaleX(-1); }

  .card__band {
    height: 115px; background: var(--brand-blue); color: var(--white);
  }
  .card--front .card__band {
    display: flex; justify-content: space-between; padding: 22px 26px 0 28px;
  }
  .person__name { font-weight: 700; font-size: 19px; letter-spacing: 0.4px; line-height: 1.1; }
  .person__role { font-size: 14.5px; line-height: 1.2; margin-bottom: 8px; }
  .person__address { font-size: 15px; line-height: 1.3; }

  .contact { list-style: none; text-align: right; font-size: 15px; line-height: 1.28; padding-top: 4px; }
  .contact li { display: flex; justify-content: flex-end; align-items: center; gap: 4px; }
  .contact svg { width: 11px; height: 11px; fill: var(--white); }

  .services {
    height: 100%; display: flex; flex-direction: column; justify-content: center;
    text-align: center; font-size: 14.5px; line-height: 1.32; padding-top: 8px;
  }

  .card__strip {
    height: 36px; background: linear-gradient(var(--strip-light), var(--strip-dark));
    color: var(--brand-blue); font-size: 13.5px; font-weight: 500;
    display: flex; align-items: center; justify-content: center; letter-spacing: 0.2px;
  }
</style>
</head>
<body>
<main class="canvas">

  <section class="card card--front">
    <header class="card__head">
      <span class="brand-mark"></span>
      <span class="brand-name">VELTRIX SOLUTIONS</span>
    </header>
    <div class="card__band">
      <div class="person">
        <p class="person__name">MARCUS HALE</p>
        <p class="person__role">Managing Director</p>
        <p class="person__address">4820 Harbor Lane<br>Country Name, 123456</p>
      </div>
      <ul class="contact">
        <li>044-555 010 200
          <svg viewBox="0 0 12 12"><path d="M1 4c0-2 2-3 5-3s5 1 5 3v1H8V4H4v1H1zM3 6h6l2 5H1z"/></svg></li>
        <li>044-555 010 200
          <svg viewBox="0 0 12 12"><path d="M3 0h6a1 1 0 0 1 1 1v10a1 1 0 0 1-1 1H3a1 1 0 0 1-1-1V1a1 1 0 0 1 1-1zm0 2v8h6V2z"/></svg></li>
        <li>info@veltrix.example
          <svg viewBox="0 0 12 12"><path d="M0 2h12v8H0zm1 1v.5l5 3 5-3V3z"/></svg></li>
        <li>www.veltrix-solutions.example
          <svg viewBox="0 0 12 12"><circle cx="6" cy="6" r="5.5"/><path d="M3 4h3v3H4zM7 7h2l-1 2z" fill="#0f1aa0"/></svg></li>
      </ul>
    </div>
    <footer class="card__strip">CONSTRUCTION ACCOUNTING SOFTWARE CONSULTANTS</footer>
  </section>

  <section class="card card--back">
    <header class="card__head">
      <span class="brand-mark"></span>
      <span class="brand-name">VELTRIX SOLUTIONS</span>
    </header>
    <div class="card__band">
      <div class="services">
        <p>New Software Implementations | Software Re-Implementations</p>
        <p>Redesigning Software Usage at the User Level</p>
        <p>Project Coordination &amp; Management | Continued Software Support</p>
      </div>
    </div>
    <footer class="card__strip">WEIGHING OPTIONS - IMPLEMENTING SOLUTIONS</footer>
  </section>

</main>
</body>
</html>
```